Business cards for a naturopathic day clinic for stem cell therapy

We need a basic design for a day clinic, that offers stem cell therapies for Lyme therapy and other severe chronic illnesses.
Our name is "Haus solvaKrĂ¤ut", which can be translated into "Manor solvaHerb". We are a couple of naturopaths working along side physiotherapists and osteopaths, yoga teachers and massage therapists. I attached our logo.

```html
<!DOCTYPE html>
<html lang="en">
<head>
<meta charset="utf-8">
<title>Haus solvaKräut – Business Cards</title>
<link href="https://fonts.googleapis.com/css2?family=Roboto:wght@300;400;500;700&display=swap" rel="stylesheet">
<style>
  :root {
    --backdrop: #ebeae8;
    --leaf: #a9bd52;
    --bark: #8a7867;
    --ink: #6b6b6b;
    --ink-strong: #5a5a5a;
    --rule: #8e8e8e;
    --paper: #fbfbfa;
  }
  html, body {
    margin: 0;
    width: 1200px;
    height: 959px;
    overflow: hidden;
    background: var(--backdrop);
    font-family: 'Roboto', Arial, sans-serif;
  }
  .sheet {
    position: relative;
    width: 1200px;
    height: 959px;
  }
  .card {
    position: absolute;
    width: 630px;
    height: 360px;
    box-shadow: 0 6px 18px rgba(0,0,0,0.12);
    overflow: hidden;
  }
  .card--front {
    left: 285px;
    top: 90px;
    background: var(--leaf);
  }
  .card--back {
    left: 285px;
    top: 510px;
    background: var(--paper);
  }
  .brand {
    position: absolute;
    display: flex;
    align-items: center;
    gap: 16px;
  }
  .brand__dot {
    border-radius: 50%;
    flex: none;
  }
  .brand__name {
    font-weight: 300;
    letter-spacing: 0.5px;
    white-space: nowrap;
  }
  .card--front .brand {
    left: 0; right: 0; top: 0; bottom: 0;
    justify-content: center;
  }
  .card--front .brand__dot {
    width: 58px; height: 58px;
    border: 3px solid #fff;
    box-sizing: border-box;
  }
  .card--front .brand__name {
    color: #fff;
    font-size: 50px;
  }
  .card--back .brand {
    right: 40px;
    top: 58px;
    gap: 12px;
  }
  .card--back .brand__dot {
    width: 34px; height: 34px;
    border: 2px solid var(--bark);
    box-sizing: border-box;
  }
  .card--back .brand__name {
    color: var(--bark);
    font-size: 30px;
  }
  .divider {
    position: absolute;
    left: 258px;
    right: 40px;
    top: 138px;
    height: 1px;
    background: var(--rule);
  }
  .person {
    position: absolute;
    left: 40px;
    top: 124px;
  }
  .person__name {
    margin: 0;
    color: var(--leaf);
    font-weight: 700;
    font-size: 20px;
    letter-spacing: 0.3px;
    text-transform: uppercase;
  }
  .person__role {
    margin: 2px 0 0;
    color: var(--ink-strong);
    font-weight: 700;
    font-size: 16px;
  }
  .contacts {
    list-style: none;
    margin: 12px 0 0;
    padding: 0;
  }
  .contacts li {
    display: flex;
    align-items: center;
    gap: 10px;
    color: var(--ink);
    font-size: 16px;
    line-height: 25px;
  }
  .contacts svg {
    width: 15px;
    height: 15px;
    flex: none;
  }
  .address {
    position: absolute;
    right: 40px;
    top: 158px;
    margin: 0;
    text-align: right;
    color: var(--ink);
    font-size: 16px;
    line-height: 22px;
    font-style: normal;
  }
  .footer-band {
    position: absolute;
    left: 0;
    bottom: 0;
    width: 630px;
    height: 24px;
  }
</style>
</head>
<body>
<main class="sheet">

  <section class="card card--front" aria-label="Card front">
    <div class="brand">
      <span class="brand__dot"></span>
      <span class="brand__name">Haus solvaKräut</span>
    </div>
  </section>

  <section class="card card--back" aria-label="Card back">
    <div class="brand">
      <span class="brand__dot"></span>
      <span class="brand__name">Haus solvaKräut</span>
    </div>

    <div class="divider"></div>

    <div class="person">
      <h1 class="person__name">Lena Marwick</h1>
      <p class="person__role">Managing Director</p>
      <ul class="contacts">
        <li>
          <svg viewBox="0 0 16 16" aria-hidden="true"><path fill="var(--leaf)" d="M3.6 1.5l2.3 2.6-1.3 1.8c.9 2 2.5 3.6 4.5 4.5l1.8-1.3 2.6 2.3-1.2 2.3C7.6 14.8 1.2 8.4 1.3 2.7z"/></svg>
          +56910293847
        </li>
        <li>
          <svg viewBox="0 0 16 16" aria-hidden="true"><rect x="1" y="3" width="14" height="10" fill="var(--leaf)"/><path d="M1.5 3.5L8 9l6.5-5.5" fill="none" stroke="#fff" stroke-width="1.2"/></svg>
          info@haus-solvakraeut.com
        </li>
        <li>
          <svg viewBox="0 0 16 16" aria-hidden="true"><g fill="none" stroke="var(--leaf)" stroke-width="1.5"><circle cx="8" cy="8" r="6.5"/><ellipse cx="8" cy="8" rx="2.8" ry="6.5"/><path d="M1.5 8h13"/></g></svg>
          www.haus-solvakraeut.com
        </li>
      </ul>
    </div>

    <address class="address">
      Haus solvaKräut, Ltd<br>
      48 Fernbrook Lane,<br>
      Aurora, ON L4G 1T5
    </address>

    <svg class="footer-band" viewBox="0 0 630 24" preserveAspectRatio="none" aria-hidden="true">
      <polygon points="0,12 450,12 444,24 0,24" fill="var(--leaf)"/>
      <polygon points="458,0 630,0 630,24 446,24" fill="var(--bark)"/>
    </svg>
  </section>

</main>
</body>
</html>
```